Word Template for KOREL Polls

KOREL Polls stands for 'Kindred Outlook Readings Entered Locally Polls'. It is a collaborative research effort to format and combine multiple sources of public opinion data from around the world into merged datasets. We need a Microsoft Word template design for our research reports, dataset codebooks, crowdsourced development guidelines, and other documents that will be produced as part of the research and development. The template should match the website design and logo, which are attached to this contest (these are the files from previous successful design contests).

The main purpose will be to write reports discussing research and analysis. There will be lots data visualizations (bar charts, scatter plots, pie charts, histograms, trend line charts etc.) as well as tables, diargams, and photos mixed in wit all the text. A second purpose will be to write guidebooks to describe processes and teach others how to manage data, find variables, and write code, which will include screenshots and Word are diagrams and figures.

There are some document uploaded as examples for the kinds of things for which we need the template (working papers, codebooks, pamphlets, etc)

Target Market(s)

academia, government, non-profits, postgraduates, researchers

Font styles to use
Serif

Colors

Designer to choose colors to be used in the design.

Requirements
Must have
• A4 size page template
• Cover page
• Must match website design and logo (see attached)
Nice to have
• Colors to match logo and website (see attached)

```html
<!DOCTYPE html>
<html lang="en">
<head>
<meta charset="utf-8">
<title>KOREL Polls – Report Template Pages</title>
<link rel="stylesheet" href="https://fonts.googleapis.com/css2?family=Open+Sans:wght@400;600;700&display=swap">
<style>
:root{
  --blue:#1a73c8;
  --blue-deep:#1565b8;
  --blue-light:#38a4ec;
  --blue-pale:#d9ebfa;
  --rule:#8fbfe8;
  --ink:#333;
  --grey:#555;
  --stage:#d4d4d4;
}
*{margin:0;padding:0;box-sizing:border-box}
html,body{width:1200px;height:1200px;overflow:hidden}
body{background:var(--stage);font-family:"Open Sans",Arial,sans-serif;color:var(--ink);position:relative}
.page{position:absolute;width:253px;height:358px;background:#fff;box-shadow:2px 3px 5px rgba(0,0,0,.25);overflow:hidden}
.page-title{position:absolute;left:22px;right:22px;top:26px;text-align:center;font-size:9px;letter-spacing:.2px;color:#222;padding-bottom:3px;border-bottom:.8px solid var(--rule)}
.body{position:absolute;left:29px;right:29px;top:50px;font-size:3.6px;line-height:5.4px;color:#444}
.body p{margin-bottom:4px}
.lead{color:var(--blue)}
.sub{font-size:6.5px;line-height:8px;color:#222;font-weight:600;margin:4px 0 1px}
.footer{position:absolute;left:0;bottom:0;width:100%;height:12px}
.footer .url{position:absolute;left:18px;top:3.5px;font-size:3.4px;color:#fff}
.footer .num{position:absolute;right:14px;top:3px;font-size:4.5px;color:#555}
.toc-head{font-size:6.5px;font-weight:700;color:var(--blue);margin-bottom:7px}
.toc-row{display:flex;align-items:flex-end;font-size:3.6px;line-height:8.5px}
.toc-row .dots{flex:1;border-bottom:.6px dotted #777;margin:0 6px 2px}
.callout{display:flex;align-items:center;gap:5px;background:var(--blue);color:#fff;padding:3px 5px;font-size:3.8px;line-height:5px;margin-bottom:6px}
.callout .icon{flex:0 0 18px;height:18px;background:#fff;border-radius:2px;display:flex;align-items:center;justify-content:center}
.grid-table{position:absolute;left:27px;right:22px;top:49px;height:255px;border:.6px solid var(--rule)}
.grid-table .head{display:flex;background:var(--blue);color:#fff;font-size:4.5px;height:9px;align-items:center}
.grid-table .head span{flex:1;padding-left:11px}
.grid-table .rows{height:246px;background:repeating-linear-gradient(#fff 0 7.2px,var(--rule) 7.2px 7.8px);position:relative}
.grid-table .rows:after{content:"";position:absolute;left:61%;top:0;bottom:0;border-left:.6px solid var(--rule)}
.data{width:100%;border-collapse:separate;border-spacing:1.5px;font-size:3.4px;margin:3px 0 6px}
.data th{background:var(--blue);color:#fff;font-weight:600;height:6px}
.data td{background:#eaeaea;height:6.5px;padding-left:4px}
.data td.c{text-align:center;padding:0}
.data tr.phase td{background:var(--blue-light);color:#fff}
.data tr.total td{background:#cfcfcf;font-weight:700}
.data tr.grand td{background:var(--blue);color:#fff}
.photo{background:linear-gradient(135deg,#6d7d8a,#3e4a52 55%,#a9b5bd)}
.cover{background:var(--blue)}
.brand{display:flex;align-items:center;gap:6px;color:#fff;font-size:16px;font-weight:600}
.brand .dot{width:11px;height:11px;border-radius:50%;background:#fff}
.cover-title{position:absolute;left:0;right:0;top:293px;text-align:center}
.cover-title .l1{font-size:12.5px;font-weight:700;color:var(--blue)}
.cover-title .l2{font-size:12.5px;font-weight:600;color:#333;margin-top:-1px}
.cover-title .l3{font-size:5.5px;font-weight:700;color:var(--blue);margin-top:5px}
ul.bul{list-style:none;margin-bottom:4px}
ul.bul li:before{content:"■ ";font-size:3px}
ul.sub-list{list-style:none;padding-left:22px;color:var(--blue)}
ul.sub-list li:before{content:"▶ ";font-size:3px}
</style>
</head>
<body>

<!-- Cover -->
<section class="page cover" style="left:38px;top:38px">
  <svg width="253" height="358" style="position:absolute;left:0;top:0">
    <polygon points="0,290 253,196 253,242 0,300" fill="var(--blue-light)"/>
    <polygon points="0,300 253,242 253,358 0,358" fill="#fff"/>
  </svg>
  <div class="brand" style="position:absolute;left:38px;top:40px"><span class="dot"></span>KOREL Polls</div>
  <div class="cover-title">
    <div class="l1">LOREM IPSUM IS SIMPLY</div>
    <div class="l2">DUMMY HAS BEEN</div>
    <div class="l3">LOREM IPSUM IS SIMPLY DUMMY HAS BEEN</div>
  </div>
</section>

<!-- Table of contents -->
<section class="page" style="left:327px;top:38px">
  <h2 class="page-title">TABLE OF CONTENTS</h2>
  <div class="body" style="left:29px;right:22px;top:74px">
    <div class="toc-head">Contents</div>
    <div class="toc-row"><span>Table of Contents</span><span class="dots"></span><span>01</span></div>
    <div class="toc-row"><span>Executive Summary</span><span class="dots"></span><span>02</span></div>
    <div class="toc-row"><span>Our Understanding of Your Needs</span><span class="dots"></span><span>02</span></div>
    <div class="toc-row"><span>Our Recommendations</span><span class="dots"></span><span>03</span></div>
    <div class="toc-row"><span>Our Approach</span><span class="dots"></span><span>05</span></div>
    <div class="toc-row"><span>Budget and Timeframe</span><span class="dots"></span><span>07</span></div>
    <div class="toc-row"><span>Appendix A: About Cedar Ridge</span><span class="dots"></span><span>10</span></div>
    <div class="toc-row"><span>Appendix B: Selected Client List</span><span class="dots"></span><span>10</span></div>
    <div class="toc-row"><span>Appendix C: Our Capabilities</span><span class="dots"></span><span>11</span></div>
    <div class="toc-row"><span>Appendix D: Our Process</span><span class="dots"></span><span>12</span></div>
  </div>
  <svg class="footer" viewBox="0 0 253 12" preserveAspectRatio="none"><polygon points="0,0 82,0 94,12 0,12" fill="var(--blue)"/><polygon points="84,0 90,0 102,12 96,12" fill="var(--blue-light)"/></svg>
  <div class="footer"><span class="url">www.korelpolls.org</span><span class="num">1</span></div>
</section>

<!-- Vision -->
<section class="page" style="left:617px;top:38px">
  <h2 class="page-title">VISION</h2>
  <div class="body" style="top:46px;left:26px;right:24px">
    <div class="callout"><span class="icon"><svg width="13" height="13" viewBox="0 0 13 13"><circle cx="6.5" cy="6.5" r="5.5" fill="none" stroke="var(--blue)" stroke-width="1.2"/><circle cx="6.5" cy="6.5" r="3" fill="none" stroke="var(--blue)" stroke-width="1"/><circle cx="6.5" cy="6.5" r="1" fill="var(--blue)"/></svg></span>Ledgerly's mission is to help and support the self-employed and small business owners with their administrative tasks so they can focus on what matters – their business.</div>
    <p class="lead">Administrative tasks are cumbersome, time-consuming and often prevent small owners from focusing their time and energy on their business and their customers. They can also be stressful for those attempting these tasks for the first time.</p>
    <p style="text-align:center">At Ledgerly, we envisage accounting for the self-employed and small business owners as being <span class="lead">automated and decentralized</span></p>
    <p>Accounting can and should be done automatically. By connecting to all sources of accounting data such as bank accounts, payment systems, e-commerce websites and invoicing systems, Ledgerly automatically completes these tasks, which would take hours to do manually. Bookings are created automatically and fully completed, and statements are available within a couple of clicks.</p>
    <p>What may seem like a pipedream to the millions of self-employed who struggle with their admin is already a reality. Now is the time to join Ledgerly on its mission.</p>
    <div class="sub">The Ledgerly model</div>
    <p>Ledgerly is based on an innovative license model that uses Token-as-a-License. The token represents lifelong software license for Ledgerly solutions. The pre-sale will enable Ledgerly to complete its development of fully automatic bookkeeping.</p>
    <p>The token sale will also pave the way for a future Ledgerly launch. Ledgerly will launch accounting on the blockchain and ensure your accounting data is comprehensive and private, but available everywhere within your preferred apps. Furthermore, a new range of business apps will connect to Ledgerly.</p>
    <p>with leading edge business data access to ensure you have the best available data at your fingertips.</p>
    <p>Ledgerly supports strong data ownership laws that truly protect individuals and ensure they have complete ownership of their data and the freedom to decide how it is used.</p>
    <p>To find out more about the Ledgerly project, please register with your email at <span class="lead">www.ledgerly.example/ico</span> so we</p>
  </div>
  <svg class="footer" viewBox="0 0 253 12" preserveAspectRatio="none"><polygon points="0,0 82,0 94,12 0,12" fill="var(--blue)"/><polygon points="84,0 90,0 102,12 96,12" fill="var(--blue-light)"/></svg>
  <div class="footer"><span class="url">www.korelpolls.org</span><span class="num">3</span></div>
</section>

<!-- Headline with chart -->
<section class="page" style="left:914px;top:38px">
  <h2 class="page-title">HEADLINE HERE</h2>
  <svg style="position:absolute;left:44px;top:62px" width="170" height="110" viewBox="0 0 170 110" font-size="3.2" fill="#555" font-family="Open Sans,sans-serif">
    <g fill="var(--blue)">
      <rect x="2" y="38.2" width="11" height="61.8"/><rect x="15" y="25.4" width="11" height="74.6"/><rect x="28" y="49.6" width="11" height="50.4"/>
      <rect x="41" y="72.7" width="11" height="27.3"/><rect x="54" y="94.3" width="11" height="5.7"/><rect x="67" y="74" width="11" height="26"/>
      <rect x="80" y="89.2" width="11" height="10.8"/><rect x="93" y="76.3" width="11" height="23.7"/><rect x="106" y="71.7" width="11" height="28.3"/>
      <rect x="119" y="43.9" width="11" height="56.1"/><rect x="132" y="33.6" width="11" height="66.4"/><rect x="145" y="2.7" width="11" height="97.3"/>
    </g>
    <g text-anchor="middle">
      <text x="7.5" y="36">120</text><text x="20.5" y="23">145</text><text x="33.5" y="47">98</text><text x="46.5" y="70">53</text><text x="59.5" y="92">11</text><text x="72.5" y="72">50.5</text>
      <text x="85.5" y="87">20.9</text><text x="98.5" y="74">46</text><text x="111.5" y="69">55</text><text x="124.5" y="41">109</text><text x="137.5" y="31">129</text><text x="150.5" y="0.5">189</text>
      <text x="7.5" y="105">Jan</text><text x="20.5" y="105">Feb</text><text x="33.5" y="105">March</text><text x="46.5" y="105">April</text><text x="59.5" y="105">May</text><text x="72.5" y="105">Jun</text>
      <text x="85.5" y="105">July</text><text x="98.5" y="105">Aug</text><text x="111.5" y="105">Sep</text><text x="124.5" y="105">Oct</text><text x="137.5" y="105">Nov</text><text x="150.5" y="105">Dec</text>
    </g>
  </svg>
  <div class="body" style="top:177px;left:28px;right:22px">
    <p class="lead">Administrative tasks are cumbersome, time-consuming and often prevent small owners from focusing their time and energy on their business and their customers. They can also be stressful for those attempting these tasks for the first time.</p>
    <p style="text-align:center">At Ledgerly, we envisage accounting for the self-employed and small business owners as being <span class="lead">automated and decentralized</span></p>
    <p>Accounting can and should be done automatically. By connecting to all sources of accounting data such as bank accounts, payment systems, e-commerce websites and invoicing systems, Ledgerly automatically completes these tasks, which would take hours to do manually.</p>
    <p>What may seem like a pipedream to the millions of self-employed who struggle with their admin is already a reality. Now is the time to join Ledgerly on its mission to transform bookkeeping.</p>
    <div class="sub">The Ledgerly model</div>
    <p>Ledgerly is based on an innovative license model that uses Token-as-a-License. The token represents lifelong software license for Ledgerly solutions and will enable fully automatic bookkeeping.</p>
    <p>The token sale will also pave the way for a future Ledgerly launch.</p>
  </div>
  <svg class="footer" viewBox="0 0 253 12" preserveAspectRatio="none"><polygon points="0,0 82,0 94,12 0,12" fill="var(--blue)"/><polygon points="84,0 90,0 102,12 96,12" fill="var(--blue-light)"/></svg>
  <div class="footer"><span class="url">www.korelpolls.org</span><span class="num">10</span></div>
</section>

<!-- Headline with blank table -->
<section class="page" style="left:38px;top:425px">
  <h2 class="page-title">HEADLINE HERE</h2>
  <div class="grid-table">
    <div class="head"><span>Lorem ipsum</span><span style="flex:.65">Lorem ipsum</span></div>
    <div class="rows"></div>
  </div>
  <svg class="footer" viewBox="0 0 253 12" preserveAspectRatio="none"><polygon points="0,0 82,0 94,12 0,12" fill="var(--blue)"/><polygon points="84,0 90,0 102,12 96,12" fill="var(--blue-light)"/></svg>
  <div class="footer"><span class="url">www.korelpolls.org</span><span class="num">9</span></div>
</section>

<!-- Understanding -->
<section class="page" style="left:327px;top:425px">
  <h2 class="page-title">OUR UNDERSTANDING OF YOUR NEEDS</h2>
  <div class="body" style="top:46px;left:29px;right:17px">
    <p>In the last two weeks of January we conducted high level conversations both with your staff and your technology partner PulseWorks. As a result of those conversations we've been able to gather the following high level goals for your project:</p>
    <p style="font-size:6px;line-height:7px;color:#666">CloudDesk must be in place to support BrightPath at launch and as the program evolves</p>
    <p class="lead" style="font-weight:600">The most critical aspect of this implementation both in terms of time sensitivity as well as functionality is centered around the support for the BrightPath project. Our current understanding of this project and how it relates to CloudDesk is as follows:</p>
    <ul class="bul"><li>BrightPath will be comprised of a series of websites focused on organizing individuals within six specific community sectors with the goal of increased institutional and public support to help the country become better prepared for a changing climate.</li><li>The primary goals of the CRM application are:</li></ul>
    <ul class="sub-list" style="margin-bottom:4px"><li>capture information of individuals and organizations (along with their respective roles)</li><li>track their progress on their site specific to-do lists and site interactions</li><li>allow GreenNation to push out next steps related to their to-do list progress and online interactions</li><li>infuse GreenNation's online and offline marketing program with useful segmentation information</li><li>natively integrate with both the BrightPath family of sites as well as GreenNation's email service provider of choice</li></ul>
    <ul class="bul"><li>The data architecture must be well defined but flexible to support the core needs of the sites at launch as well as anticipated needs in the future.</li></ul>
    <ul class="sub-list" style="margin-bottom:4px"><li>For instance, the faith based site may collect a "denomination" field, while other sites may not collect that field.</li><li>Future interactions outside of the to-do list may become necessary to track and GreenNation will need a systemic way to capture those interactions and provide automated marketing around those similar to the to-do list</li></ul>
    <ul class="bul"><li>The information collected from the BrightPath sites must be combined with current information held within GreenNation and provide a holistic view of institutions and individuals.</li></ul>
  </div>
  <svg class="footer" viewBox="0 0 253 12" preserveAspectRatio="none"><polygon points="0,0 82,0 94,12 0,12" fill="var(--blue)"/><polygon points="84,0 90,0 102,12 96,12" fill="var(--blue-light)"/></svg>
  <div class="footer"><span class="url">www.korelpolls.org</span><span class="num">6</span></div>
</section>

<!-- Budget -->
<section class="page" style="left:617px;top:425px">
  <h2 class="page-title">BUDGET AND TIMEFRAME</h2>
  <div class="body" style="top:43px;left:28px;right:24px">
    <div class="sub" style="margin-top:0">Implementation Estimate</div>
    <p>The bulk of the implementation costs will be defined by discovery. Based on similar CRM implementation projects, we feel expect that the CRM side will be somewhere between 200 and 300 hours, give or take. The wide swing in hours in phase one is related to the ill-defined nature of both the integration needs and our role in the integration project. Our focus in discovery will be to nail down those requirements and our role as it relates to what is needed to integrate the sites with the CRM.</p>
    <table class="data">
      <tr><th style="width:50%">Task</th><th>Hours</th><th>Cost</th></tr>
      <tr><td>Discovery</td><td class="c">40</td><td class="c">$8,000</td></tr>
      <tr class="phase"><td>Phase 1</td><td></td><td></td></tr>
      <tr><td>Discovery</td><td class="c">20-40</td><td class="c">$8,000</td></tr>
      <tr><td>Discovery</td><td class="c">20-40</td><td class="c">$8,000</td></tr>
      <tr><td>Discovery</td><td class="c">20-40</td><td class="c">$8,000</td></tr>
      <tr class="total"><td>Total Phase 1</td><td class="c">80-240</td><td class="c">$16,800-40,000</td></tr>
      <tr class="phase"><td>Phase 2</td><td></td><td></td></tr>
      <tr><td>Discovery</td><td class="c">20-40</td><td class="c">$8,000</td></tr>
      <tr class="total"><td>Total Phase 2</td><td class="c">80-240</td><td class="c">$16,800-40,000</td></tr>
      <tr class="grand"><td>Total Estimated Implementation Cost</td><td class="c">220-480</td><td class="c">$44,000-96,000</td></tr>
    </table>
    <div class="sub">Project Timeline</div>
    <p>Based on the information we have at our disposal, the March 21st launch date doesn't seem a realistic goal to get both the work done needed to provide the foundation for the future CRM instance and the integration given the state of apparent flux of the requirements. That said, we feel it prudent to proceed with discovery before committing to pushing that date. We are currently estimating that the first phase will take somewhere between 7 and 12 weeks (including discovery) to complete.</p>
    <table class="data" style="width:80%">
      <tr><th style="width:60%">Task</th><th>Weeks to Complete</th></tr>
      <tr><td>Discovery</td><td class="c">1-2</td></tr>
      <tr><td>Phase 1</td><td class="c">6-10</td></tr>
      <tr><td>Phase 2</td><td class="c">8-12</td></tr>
      <tr class="total"><td>Total Number of Weeks</td><td></td></tr>
    </table>
  </div>
  <svg class="footer" viewBox="0 0 253 12" preserveAspectRatio="none"><polygon points="0,0 82,0 94,12 0,12" fill="var(--blue)"/><polygon points="84,0 90,0 102,12 96,12" fill="var(--blue-light)"/></svg>
  <div class="footer"><span class="url">www.korelpolls.org</span><span class="num">5</span></div>
</section>

<!-- Headline with photo -->
<section class="page" style="left:914px;top:421px">
  <h2 class="page-title">HEADLINE HERE</h2>
  <div class="photo" role="img" aria-label="Photo of a stressed businessman at a desk, hand on forehead" style="position:absolute;left:28px;top:45px;width:203px;height:90px"></div>
  <div class="body" style="top:142px;left:28px;right:22px">
    <p class="lead">Ledgerly's mission is to help and support the self-employed and small business owners with their administrative tasks so they can focus on what matters – their business.</p>
    <p>Administrative tasks are cumbersome, time-consuming and often prevent small owners from focusing their time and energy on their business and their customers. They can also be extremely stressful for those attempting these tasks for the first time.</p>
    <p>At Ledgerly, we envisage accounting for the self-employed and small business owners as being <span class="lead">automated and decentralized</span></p>
    <p>Accounting can and should be done automatically. By connecting to all sources of accounting data such as bank accounts, payment systems, e-commerce websites and invoicing systems, Ledgerly automatically completes these tasks, which would take hours to do manually. Statements are available within a couple of clicks.</p>
    <p>What may seem like a pipedream to the millions of self-employed who struggle with their admin is already a reality. Now is the time to join Ledgerly on its mission.</p>
    <div class="sub">The Ledgerly model</div>
    <p>Ledgerly is based on an innovative license model that uses Token-as-a-License. The token represents lifelong software license for Ledgerly solutions and enables fully automatic bookkeeping.</p>
    <p>with leading edge business data access to ensure you have the best available data at your fingertips.</p>
  </div>
  <svg class="footer" viewBox="0 0 253 12" preserveAspectRatio="none"><polygon points="0,0 82,0 94,12 0,12" fill="var(--blue)"/><polygon points="84,0 90,0 102,12 96,12" fill="var(--blue-light)"/></svg>
  <div class="footer"><span class="url">www.korelpolls.org</span><span class="num">7</span></div>
</section>

<!-- Headline with two photos -->
<section class="page" style="left:38px;top:812px">
  <h2 class="page-title">HEADLINE HERE</h2>
  <div class="photo" role="img" aria-label="Photo of a worried businessman holding his head" style="position:absolute;left:29px;top:45px;width:86px;height:112px"></div>
  <div class="photo" role="img" aria-label="Photo of a businessman sitting with head in hand" style="position:absolute;left:29px;top:202px;width:86px;height:128px"></div>
  <div class="body" style="top:45px;left:126px;right:22px">
    <p class="lead">Ledgerly's mission is to help and support the self-employed and small business owners with their administrative tasks so they can focus on what matters – their business.</p>
    <p>Administrative tasks are cumbersome, time-consuming and often prevent small owners from focusing their time and energy on their business and their customers. They can also be extremely stressful for those attempting these tasks for the first time.</p>
    <p>At Ledgerly, we envisage accounting for the self-employed and small business owners as being <span class="lead">automated and decentralized</span></p>
    <p>Accounting can and should be done automatically. By connecting to all sources of accounting data such as bank accounts, payment systems, e-commerce websites and invoicing systems, Ledgerly automatically completes these tasks, which would take hours to do manually. Bookings are created automatically and fully completed. Financial statements are available within a couple of clicks, and after analysing your data, Ledgerly will offer you tips to improve your financial stability.</p>
    <p>What may seem like a pipedream to the millions of self-employed who struggle with</p>
    <div class="sub" style="color:var(--blue)">The Ledgerly model</div>
    <p>Ledgerly is based on an innovative license model that uses Token-as-a-License. The token represents lifelong software license for Ledgerly solutions. The token sales will enable Ledgerly to complete its development of fully automatic bookkeeping.</p>
  </div>
  <svg class="footer" viewBox="0 0 253 12" preserveAspectRatio="none"><polygon points="0,0 82,0 94,12 0,12" fill="var(--blue)"/><polygon points="84,0 90,0 102,12 96,12" fill="var(--blue-light)"/></svg>
  <div class="footer"><span class="url">www.korelpolls.org</span><span class="num">8</span></div>
</section>

<!-- Solution -->
<section class="page" style="left:325px;top:812px">
  <h2 class="page-title">HEADLINE HERE</h2>
  <div class="body" style="top:46px;left:26px;right:24px">
    <div class="sub">Solution</div>
    <p><span class="lead">AI automated accounting</span><br>Ledgerly builds automation in stages on top of its current system to reach full automation thanks to the Ledgerly AI. Ledgerly AI automates every manual task performed by the user. It starts by connecting to all sources of accounting data such as bank accounts, credit card, webshop or document management systems (FileVault or CloudCrate). Based on these data, Ledgerly AI creates bookings and generates financial reports. Finally, a chat-like interface allows users to communicate seamlessly with it, viewing it as a trusted advisor over time for all their accounting queries.</p>
    <p><span class="lead">Blockchain software license or Token-as-a-License</span><br>It is possible to create tokens on blockchain that represent software licenses, also known as Token-as-a-License. Ledgerly creates tokens by using the Nimbus official wallet which interacts with the Nimbus blockchain. Upon purchase, the token holder is free to transfer or sell it, using a secondary market that is built directly over the blockchain. Ledgerly checks the validity of a token against the blockchain ensuring that token holders have access to the Ledgerly solutions. This makes distribution and securisation of software licenses easier for developers and easier for owners. All in all, a token has a higher value as a normal software license.</p>
    <div class="sub">Pre-Sale Token sale</div>
    <p>To realize this innovative vision, Ledgerly is launching a pre-sale in form of a token sale on Nimbus blockchain. 20,000,000 tokens are available to purchase for the price of 0.10 each during a 30-day period to be announced. Tokens represent Ledgerly lifelong software licenses and by purchasing enough tokens, holders gain access to Ledgerly software. 15,000 tokens give access to Ledgerly invoicing or accounting, 20,000 tokens give access to both. Future customers will still have the opportunity to buy directly yearly or monthly subscriptions.</p>
    <div class="sub">Future plans</div>
    <p>A future launch is planned between 18 and 24 months after the pre-sale token sale. This offering will support the development of Ledgerly into a fully decentralized, privacy-focused ecosystem of applications. The new model will reward each participant so that a new world with zero administrative tasks becomes reality.</p>
  </div>
  <svg class="footer" viewBox="0 0 253 12" preserveAspectRatio="none"><polygon points="0,0 82,0 94,12 0,12" fill="var(--blue)"/><polygon points="84,0 90,0 102,12 96,12" fill="var(--blue-light)"/></svg>
  <div class="footer"><span class="url">www.korelpolls.org</span><span class="num">2</span></div>
</section>

<!-- Back cover -->
<section class="page cover" style="left:611px;top:812px">
  <svg width="253" height="358" style="position:absolute;left:0;top:0">
    <polygon points="0,286 253,196 253,226 0,300" fill="var(--blue-light)"/>
    <polygon points="0,300 253,226 253,358 0,358" fill="#fff"/>
  </svg>
  <div style="position:absolute;left:28px;top:320px;display:flex;align-items:center;gap:4px;color:var(--blue);font-size:7.5px;font-weight:600"><span style="width:6px;height:6px;border-radius:50%;background:var(--blue)"></span>KOREL Polls</div>
  <div style="position:absolute;left:112px;top:314px;height:22px;border-left:.6px solid var(--rule)"></div>
  <div style="position:absolute;left:117px;top:314px;font-size:2.8px;line-height:4.6px;color:var(--blue)">
    <div>● 000-555-0142 Ext 101</div><div>● hello@korelpolls.org</div><div>● www.korelpolls.org</div>
  </div>
  <div style="position:absolute;left:172px;top:316px;font-size:2.8px;line-height:4.2px;color:var(--blue)">300, 1200 Harbour Street<br>Riverton, Northland R1V 2B3</div>
</section>

</body>
</html>
```